Business Card Design Project

Our organization is in need of a business card design with the use of our logo. We are looking for professional design that will embellish the image our consulting firm.

Here is a summary of what we do: Quorvent is systems consulting firm that specializes in the management, migration, and maintenance of IT infrastructure solutions.

Here is a link to my website: http://quorvent-example.com

I have attached the logo.

Target Market(s)

Organization that need IT and server support.

Industry/Entity Type

Business

```html
<!DOCTYPE html>
<html lang="en">
<head>
<meta charset="utf-8">
<title>Quorvent Business Card</title>
<link href="https://fonts.googleapis.com/css2?family=Questrial&display=swap" rel="stylesheet">
<style>
  :root {
    --backdrop: #dcdcdc;
    --card: #ffffff;
    --navy: #1f2a5c;
  }
  * { margin: 0; padding: 0; box-sizing: border-box; }
  html, body {
    width: 867px;
    height: 1200px;
    overflow: hidden;
    background: var(--backdrop);
    font-family: "Questrial", "Century Gothic", sans-serif;
    color: var(--navy);
  }
  .canvas { position: relative; width: 867px; height: 1200px; }
  .card {
    position: absolute;
    left: 28px;
    width: 816px;
    height: 528px;
    background: var(--card);
  }
  .card--front { top: 25px; }
  .card--back { top: 650px; }

  .brand-lockup {
    position: absolute;
    left: 334px;
    top: 252px;
    display: flex;
    align-items: center;
    gap: 22px;
  }
  .brand-mark { width: 46px; height: 46px; }
  .brand-name { font-size: 56px; line-height: 1; letter-spacing: -0.5px; }

  .company-block { position: absolute; left: 60px; top: 54px; }
  .company-name { font-size: 34px; line-height: 1.05; margin-bottom: 4px; }
  .address { font-style: normal; font-size: 27px; line-height: 33px; letter-spacing: -0.3px; }

  .contact-list {
    position: absolute;
    left: 60px;
    top: 372px;
    display: grid;
    grid-template-columns: 58px auto;
    font-size: 28px;
    line-height: 35px;
    letter-spacing: -0.2px;
  }
  .contact-label { padding-left: 4px; }
</style>
</head>
<body>
<div class="canvas">
  <section class="card card--front">
    <div class="brand-lockup">
      <svg class="brand-mark" viewBox="0 0 46 46" aria-hidden="true">
        <circle cx="23" cy="23" r="22" fill="var(--navy)"/>
      </svg>
      <span class="brand-name">Quorvent</span>
    </div>
  </section>

  <section class="card card--back">
    <div class="company-block">
      <div class="company-name">Quorvent</div>
      <address class="address">
        4120 Cedar Loop<br>
        San Antonio<br>
        TX 78201
      </address>
    </div>
    <div class="contact-list">
      <span class="contact-label">f</span><span class="contact-value">210.555.0142</span>
      <span class="contact-label">t</span><span class="contact-value">1.888.555.0190</span>
      <span class="contact-label">w</span><span class="contact-value">quorvent-example.com</span>
    </div>
  </section>
</div>
</body>
</html>
```